New Template design for Website in Wordpress

We are interested in changing our website look at www.haulvantix.com -We also are very interested in Have it done in Wordpress in which we are understanding the search engines are liking a bit more. The website we would want to try working with on this is www.haulvantix.com. We look forward to seeing the different design ideas please just make sure they are in wordpress! Thanks, Merrick

Reason: need more design idea..... We would still like to use our pictures off our site since we paid for them so keep that in mind as well as we would still want the rotating pictures in the head of the page but not in Flash.

```html
<!DOCTYPE html>
<html lang="en">
<head>
<meta charset="utf-8">
<title>Haulvantix – A Diversified Freight Company</title>
<link href="https://fonts.googleapis.com/css2?family=Open+Sans:wght@400;600;700&display=swap" rel="stylesheet">
<style>
:root{
  --page-dark:#2a2a2a;
  --page-light:#ebebeb;
  --header:#000;
  --white:#fff;
  --red:#b8322f;
  --red-line:#c7403b;
  --ink:#2b2b2b;
  --muted:#6b6b6b;
  --footer-bar:#d4d4d4;
  --nav:#b5b5b5;
  --sky-deep:#1f7ad6;
  --sky-light:#8cc4ef;
  --snow:#eef1f3;
  --road:#7d7a76;
}
*{margin:0;padding:0;box-sizing:border-box}
html,body{width:761px;height:1200px;overflow:hidden}
body{font-family:"Open Sans",Arial,sans-serif;color:var(--ink);
  background:linear-gradient(var(--page-dark) 0 508px,var(--page-light) 508px);position:relative}
.abs{position:absolute}
.site-header{left:63px;top:0;width:635px;height:79px;background:var(--header);color:var(--white)}
.brand{left:14px;top:14px;font-size:30px;font-weight:700;letter-spacing:.5px;line-height:1}
.tagline{left:14px;top:50px;font-size:12.5px;color:#ddd;letter-spacing:.2px}
.social{left:414px;top:22px;display:flex;gap:12px}
.social span{width:10px;height:10px;border-radius:50%;background:#bbb;display:block}
.call{left:497px;top:19px;font-size:13.5px;color:#ddd}
.nav{top:51px;font-size:9.5px;color:var(--nav);letter-spacing:.2px}
.nav.active{color:var(--white);font-weight:600}
.hero{left:63px;top:79px;width:635px;height:429px;overflow:hidden;
  background:
    radial-gradient(ellipse 150px 150px at 330px 250px,rgba(70,80,95,.55),rgba(70,80,95,0) 100%),
    radial-gradient(ellipse 260px 120px at 420px 400px,rgba(90,86,80,.6),rgba(90,86,80,0) 100%),
    linear-gradient(var(--sky-deep) 0%,#4a9ce6 18%,var(--sky-light) 34%,var(--snow) 44%,#e2e5e8 58%,#b9bbbc 74%,var(--road) 100%)}
.hero-cue{left:282px;top:196px;width:72px;height:56px;opacity:.6}
.hero-title{left:0;top:16px;width:635px;text-align:center;color:var(--white);font-size:22px;font-weight:600;letter-spacing:.5px}
.hero-sub{left:0;top:45px;width:635px;text-align:center;color:var(--white);font-size:9.5px}
.hero-sub u{font-weight:600}
.slide-arrow{top:193px;width:34px;height:42px;background:rgba(170,170,170,.7);display:flex;align-items:center;justify-content:center}
.content{left:63px;top:508px;width:635px;height:376px;background:var(--white)}
.h-red{width:635px;text-align:center;color:var(--red);font-size:16px;font-weight:700}
.h-dark{left:0;top:54px;width:635px;text-align:center;font-size:13px;font-weight:700;letter-spacing:.3px}
.intro{left:22px;top:77px;width:591px;text-align:center;font-size:8.6px;line-height:15.2px;color:var(--muted)}
.rule{top:148px;height:1px;background:#ddd}
.btn-more{left:284px;top:137px;width:67px;height:23px;background:#555;color:#fff;font-size:8.5px;text-align:center;line-height:23px;border-radius:2px}
.service{top:214px;width:150px}
.service .ph{height:86px}
.service p{margin-top:13px;text-align:center;font-size:10.5px;font-weight:600;line-height:14.5px}
.red-line{left:63px;top:883px;width:635px;height:3px;background:var(--red-line)}
.btn-quote{left:294px;top:870px;width:166px;height:29px;background:var(--red);color:#fff;font-size:12px;text-align:center;line-height:29px;border-radius:3px}
.fcol h4{font-size:10px;font-weight:600;line-height:14px;color:var(--ink)}
.fcol ul{list-style:none;margin-top:7px}
.fcol li{font-size:8px;line-height:15.2px;color:var(--muted);padding-left:7px;position:relative}
.fcol li:before{content:"•";position:absolute;left:0;font-size:7px}
.foot-bar{left:0;top:1160px;width:761px;height:40px;background:var(--footer-bar);text-align:center;font-size:9px;line-height:40px;color:var(--muted)}
</style>
</head>
<body>
<header class="site-header abs">
  <div class="brand abs">HAULVANTIX</div>
  <div class="tagline abs">A DIVERSIFIED FREIGHT COMPANY</div>
  <div class="social abs"><span></span><span></span><span></span></div>
  <div class="call abs">Call : (555)014-2270</div>
  <div class="nav active abs" style="left:357px">HOME</div>
  <div class="nav abs" style="left:414px">INSURANCE &amp; LEGAL INFO</div>
  <div class="nav abs" style="left:560px">GET A QUOTE</div>
</header>

<section class="hero abs" role="img" aria-label="Slider photo: tanker truck driving along a snowy highway under a blue sky">
  <svg class="hero-cue abs" viewBox="0 0 72 56" aria-hidden="true">
    <rect x="2" y="2" width="68" height="52" rx="4" fill="none" stroke="#fff" stroke-width="3"/>
    <circle cx="52" cy="17" r="6" fill="#fff"/>
    <path d="M6 50 26 26l13 15 8-9 19 18z" fill="#fff"/>
  </svg>
  <div class="hero-title abs">WORLDWIDE SHIPPING</div>
  <div class="hero-sub abs">Trucking and Ocean Service with No Limits - <u>Click Here for Freight Quote</u></div>
  <div class="slide-arrow abs" style="left:0"><svg width="14" height="24" viewBox="0 0 14 24"><path d="M12 2 2 12l10 10" fill="none" stroke="#fff" stroke-width="1.5"/></svg></div>
  <div class="slide-arrow abs" style="left:601px"><svg width="14" height="24" viewBox="0 0 14 24"><path d="M2 2l10 10L2 22" fill="none" stroke="#fff" stroke-width="1.5"/></svg></div>
</section>

<main class="content abs">
  <h1 class="h-red abs" style="left:0;top:28px">GET FAST &amp; FREE FREIGHT QUOTES NOW AND SAVE!!</h1>
  <h2 class="h-dark abs">WORLDWIDE SHIPPING- OCEAN AND TRUCKING WITH NO LIMITS</h2>
  <p class="intro abs">Welcome to Haulvantix and Vantix Cargo Inc. We are a one stop solution logistics company servicing Worldwide with our Trucking and Ocean shipping service. In using our freight services, we will negotiate a competitive freight quote using over 5000 different carriers who are certified and contracted by us. We have all equipment types available daily, service all freight types, and have no limits Worldwide.</p>
  <div class="rule abs" style="left:6px;width:270px"></div>
  <div class="rule abs" style="left:359px;width:270px"></div>
  <div class="btn-more abs">READ MORE</div>
  <h2 class="h-red abs" style="left:0;top:185px">WHAT WE DO</h2>
  <div class="service abs" style="left:7px"><div class="ph" role="img" aria-label="Heavy mining loader on a red lowboy truck" style="background:linear-gradient(135deg,#c9a62c,#6f7a3a 60%,#a33a2f)"></div><p>HEAVY HAUL<br>SERVICES</p></div>
  <div class="service abs" style="left:164px"><div class="ph" role="img" aria-label="White semi truck with a dry van trailer" style="background:linear-gradient(#f2f2f2,#c7c9cb 70%,#555)"></div><p>DRY &amp; REFRIGERATED<br>SERVICES</p></div>
  <div class="service abs" style="left:321px"><div class="ph" role="img" aria-label="Blue truck pulling a flatbed trailer on a highway" style="background:linear-gradient(#8a8f86,#5d6a4a 45%,#4a5a8a)"></div><p>FLATBED, STEP DECK &amp;<br>PIGGY BACK SERVICE</p></div>
  <div class="service abs" style="left:478px"><div class="ph" role="img" aria-label="Container ship at sea" style="background:linear-gradient(#dfe8ef,#5f7fa3 55%,#2f4a6b)"></div><p>FREIGHT FORWARDING<br>OCEAN SERVICES</p></div>
</main>

<div class="red-line abs"></div>
<div class="btn-quote abs">GET A FREIGHT QUOTE</div>

<div class="fcol abs" style="left:65px;top:920px"><h4>WORLDWIDE FREIGHT<br>SERVICES</h4><ul><li>Worldwide Shipping Scope</li><li>Trucking Shipping Services</li><li>Ocean Shipping Services</li><li>Insurance &amp; Legal Details</li><li>Get a Freight Quote Now!</li><li>Return to Home Page</li></ul></div>
<div class="fcol abs" style="left:210px;top:920px"><h4>FREIGHT - TRUCKING<br>SERVICE</h4><ul><li>Heavy Equipment Hauling</li><li>LTL Freight Transport</li><li>Flatbed Transport</li><li>Step Deck Transport</li><li>Dry Van Transport</li><li>Refrigerated Transport</li><li>Power Only &amp; Towaway Transport</li></ul></div>
<div class="fcol abs" style="left:376px;top:920px"><h4>OCEAN SHIPPING<br>SERVICES</h4><ul><li>Heavy Equipment Hauling</li><li>LTL Freight Transport</li><li>Flatbed Transport</li><li>Step Deck Transport</li><li>Dry Van Transport</li><li>Refrigerated Transport</li><li>Power Only &amp; Towaway Transport</li></ul></div>
<div class="fcol abs" style="left:548px;top:920px"><h4>WE SHIP IT ALL<br>WORLDWIDE!</h4><ul><li>Full Loads</li><li>LTL-Less Then Full Loads</li><li>Oversized &amp; Overweight Loads</li><li>500 LBS to 200,000 LBS (No Limits)</li><li>Construction &amp; Mining Equipment</li><li>Mills &amp; Machinery</li><li>Hay &amp; Alfalfa</li><li>Agriculture Equipment &amp; Commodities</li><li>Vehicles, Semi Tractors and Trailers</li><li>Military and Non-Military Equipment</li><li>Refrigerated &amp; Dry Goods of All Kinds</li><li>Tanks, Waste Equipment, and More!</li></ul></div>
<div class="fcol abs" style="left:65px;top:1075px"><h4>POPULAR PAGES</h4><ul><li>Equipment Transport</li><li>Equipment Hauling</li><li>Shipping Service Areas</li></ul></div>
<div class="fcol abs" style="left:211px;top:1075px"><h4>LINK PAGES</h4><ul><li>Home</li><li>Insurance &amp; Legal Info</li><li>Get a Quote</li></ul></div>
<div class="fcol abs" style="left:375px;top:1075px"><h4>CONTACT US</h4><ul><li>Call : (555)014-2270</li><li>E-mail : info@haulvantix.com</li></ul></div>

<footer class="foot-bar abs">Copyright © 2014 Haulvantix. &nbsp;All rights reserved. &nbsp;Sitemap &nbsp;/ &nbsp;Privacy Policy</footer>
</body>
</html>
```